Halvane Lift Works Brochure

I am looking for a multi page brochure that outlines what we do, our services, and our equipment.
We are committed to delivering equipment, operators, and technicians that provide safe, experienced, and reliable access at heights, industrial sites, power lines/facilities, construction, refineries, and other similar type industries across North America.
Our truck mounted aerial lift platforms are the preferred method of servicing at height structures and industrial plants due to their quick setup, unmatched safety, and ability to operate in adverse conditions.
Incorporate the attached images into the brochure. The overall layout should be a couple pages about us, including our commitment to safe work practices, then about the units themselves.
You can get more information from our website www.halvanelift-example.com
Our tagline is Safety. Quality. Service.
Colouring for the brochure should complement our red logo. Our logo could also be used as white.

```html
<!DOCTYPE html>
<html lang="en">
<head>
<meta charset="utf-8">
<title>Halvane Lift Works Brochure</title>
<link href="https://fonts.googleapis.com/css2?family=Raleway:wght@500;600;700;800&display=swap" rel="stylesheet">
<style>
  :root {
    --brand-red: #d0222b;
    --panel-dark: #303030;
    --text-light: #ffffff;
  }
  * { margin: 0; padding: 0; box-sizing: border-box; }
  html, body { width: 1200px; height: 848px; overflow: hidden; background: var(--panel-dark); }
  .brochure {
    position: relative; width: 1200px; height: 848px;
    background: var(--panel-dark); color: var(--text-light);
    font-family: "Raleway", Arial, sans-serif;
  }
  .band { position: absolute; left: 0; width: 100%; height: 14px; background: var(--brand-red); }
  .band--top { top: 0; }
  .band--bottom { bottom: 0; }
  .block { position: absolute; }
  .body-copy {
    font-size: 20px; font-weight: 500; line-height: 27px;
    hyphens: auto; -webkit-hyphens: auto;
  }
  .heading {
    display: flex; align-items: center; gap: 14px;
    font-weight: 800; font-size: 52px; line-height: 56px; letter-spacing: -0.5px;
  }
  .heading .accent { color: var(--brand-red); }
  .marker { flex: none; }
  .heading--stack { display: block; }
  .heading--stack .row { display: flex; align-items: center; gap: 14px; }
  .spaced { letter-spacing: 7px; padding-left: 44px; }
  .subheading {
    display: flex; align-items: flex-start; gap: 18px;
    font-weight: 700; font-size: 34px; line-height: 42px;
  }
  .subheading .marker { margin-top: 10px; }
</style>
</head>
<body>
<main class="brochure">
  <div class="band band--top"></div>
  <div class="band band--bottom"></div>

  <!-- Column one -->
  <h1 class="block heading heading--stack" style="left:20px; top:26px;">
    <span class="row">
      <svg class="marker" width="28" height="26" viewBox="0 0 28 26"><polygon points="0,0 28,13 0,26" fill="var(--brand-red)"/></svg>
      <span>Company</span>
    </span>
    <span class="row accent spaced">Profile</span>
  </h1>
  <p class="block body-copy" style="left:20px; top:146px; width:375px;">
    We are a specialized company dedicated to the success of the renewables industry<br>
    With over 65+ years of combined experience in equipment operation and project managment, we are uniquely positioned to ensure the success of your projects. We specialize in blade access but have also worked, and are certified to provide services in oil and gas and refineries. We are able to provide the most stable access to wind turbine blades, flare stacks, utility lines, high rises and many other complex project scopes required in industry.
  </p>

  <h2 class="block heading" style="left:20px; top:580px;">
    <svg class="marker" width="28" height="26" viewBox="0 0 28 26"><polygon points="0,0 28,13 0,26" fill="var(--brand-red)"/></svg>
    <span>Our&nbsp; <span class="accent">Vision</span></span>
  </h2>
  <p class="block body-copy" style="left:20px; top:641px; width:375px;">
    We are committed to providing unparalleled service and access to the renewables and wind industries. Our equipment is top-of-line in safety and reliability ensuring that our customers receive the best in-class service.
  </p>

  <!-- Column two -->
  <p class="block body-copy" style="left:415px; top:36px; width:375px;">
    Our operators and technicians are provided premier training to ensure they are able to perform safely in any situation. Customer satisfaction is paramount in our values and we are committed to the success of your project however large or small.
  </p>

  <h2 class="block heading" style="left:415px; top:236px;">
    <svg class="marker" width="28" height="26" viewBox="0 0 28 26"><polygon points="0,0 28,13 0,26" fill="var(--brand-red)"/></svg>
    <span>Our <span class="accent">Solution</span></span>
  </h2>
  <p class="block body-copy" style="left:415px; top:298px; width:375px;">
    We offer a unique solution that includes a fully transparent costing model with new equipment, highly experienced operators, and a complete dedication to reliablity and safety.
  </p>

  <h2 class="block heading heading--stack" style="left:415px; top:442px;">
    <span class="row">
      <svg class="marker" width="28" height="26" viewBox="0 0 28 26"><polygon points="0,0 28,13 0,26" fill="var(--brand-red)"/></svg>
      <span>Our</span>
    </span>
    <span class="row accent" style="padding-left:44px;">Services</span>
  </h2>
  <h3 class="block subheading" style="left:415px; top:564px;">
    <svg class="marker" width="26" height="24" viewBox="0 0 26 24"><polygon points="0,0 26,12 0,24" fill="var(--text-light)"/></svg>
    <span>Blade Access</span>
  </h3>
  <p class="block body-copy" style="left:415px; top:614px; width:375px;">
    We provide industry leading truck mounted aerial access services using Talveria trucks. Our trucks are all less than 2 years old ensuring reliability on your project. We understand the criticality of reliability and our commitment is that your project will not
  </p>

  <!-- Column three -->
  <p class="block body-copy" style="left:808px; top:36px; width:378px;">
    be delayed as a result of equipment failure.
  </p>
  <h3 class="block subheading" style="left:808px; top:102px; font-size:36px; line-height:44px;">
    <svg class="marker" width="26" height="24" viewBox="0 0 26 24"><polygon points="0,0 26,12 0,24" fill="var(--text-light)"/></svg>
    <span>Supplimentary<br><span style="margin-left:-44px; padding-left:0;">&nbsp;</span></span>
  </h3>
  <h3 class="block subheading" style="left:852px; top:146px; font-size:36px; line-height:44px;">
    <span>Resource Support</span>
  </h3>
  <p class="block body-copy" style="left:808px; top:204px; width:378px;">
    As an experienced wind service provider, our goal is to provide your industry with the best trained and motivated technicians to ensure your service and maintenance needs are met with quality and on schedule. Our biggest success is when your company finds our technicians are high enough caliber to bring on board and integrate within your service organization.<br>
    Our goal is also to ensure that the technicians that we provide are adequately trained and are able to integrate with your site service teams seamlessly. We only hire the highest performing technicians and ensure they are provided every opportunity for growth within their respective industries.
  </p>
</main>
</body>
</html>
```